Breezeway Climate Business Card Design

Design new, 2 sides, business cards for a residential and light commercial heating, air conditioning contractor.

Target Market(s)

Homeowners, small businesses

Industry/Entity Type

Business

Contact Information for Business Card

Dominic Vasquerelli
Phone - 555-214-6837
Email
Address - PO box 618
Millbrook NJ 07999
Website - www.BreezewayClimateLLC.example

Requirements
Must have
• logo, company colors, standard size with no die cut, so I can use printhaven

```html
<!DOCTYPE html>
<html lang="en">
<head>
<meta charset="utf-8">
<title>Breezeway Climate – Business Cards</title>
<link href="https://fonts.googleapis.com/css2?family=Lato:wght@400;700&display=swap" rel="stylesheet">
<style>
  :root {
    --brand-red: #9c2232;
    --brand-orange: #f08a24;
    --paper: #ffffff;
    --ink: #3a3a3a;
    --backdrop: #2e2e30;
  }
  * { margin: 0; padding: 0; box-sizing: border-box; }
  html, body {
    width: 1200px; height: 814px; overflow: hidden;
    background: var(--backdrop);
    font-family: "Lato", sans-serif;
  }
  .canvas { position: relative; width: 1200px; height: 814px; }
  .card {
    position: absolute; width: 520px; height: 297px; overflow: hidden;
    box-shadow: 0 8px 24px rgba(0,0,0,.45);
  }
  /* Back side */
  .card-back { left: 70px; top: 90px; background: var(--brand-red); }
  .card-back .brand-mark {
    position: absolute; left: 0; right: 0; top: 100px;
    display: flex; align-items: center; justify-content: center; gap: 12px;
    color: var(--paper); font-weight: 700; font-size: 34px;
  }
  .brand-dot { width: 18px; height: 18px; border-radius: 50%; background: currentColor; flex: none; }
  .card-back .website {
    position: absolute; left: 0; right: 0; bottom: 34px; text-align: center;
    color: var(--paper); font-size: 15px;
  }
  /* Front side */
  .card-front { left: 610px; top: 420px; background: var(--paper); }
  .card-front .brand-mark {
    position: absolute; left: 34px; top: 92px;
    display: flex; align-items: center; gap: 10px;
    color: var(--brand-red); font-weight: 700; font-size: 26px;
  }
  .card-front .brand-dot { background: var(--brand-orange); }
  .contact-list {
    position: absolute; right: 28px; top: 28px; list-style: none;
    font-size: 12.5px; line-height: 19px; color: var(--ink); text-align: right;
  }
  .contact-list li { display: flex; justify-content: flex-end; align-items: center; gap: 8px; }
  .contact-list svg { width: 11px; height: 11px; fill: var(--brand-red); flex: none; }
  .contact-list .spacer { width: 11px; }
  .holder-name {
    position: absolute; left: 34px; top: 178px;
    color: var(--brand-red); font-weight: 700; font-size: 22px;
  }
  .wave { position: absolute; left: 0; bottom: 0; width: 520px; height: 297px; }
</style>
</head>
<body>
<main class="canvas">
  <section class="card card-back" aria-label="Card back">
    <div class="brand-mark"><span class="brand-dot"></span>Breezeway Climate</div>
    <p class="website">www.BreezewayClimateLLC.example</p>
  </section>

  <section class="card card-front" aria-label="Card front">
    <svg class="wave" viewBox="0 0 520 297" aria-hidden="true">
      <path d="M0 272 C150 255 300 215 400 150 C450 118 490 110 520 108 L520 297 L0 297 Z" fill="var(--brand-red)"/>
      <path d="M0 262 C150 245 280 215 360 160 C300 212 160 252 0 272 Z" fill="var(--brand-orange)"/>
    </svg>

    <div class="brand-mark"><span class="brand-dot"></span>Breezeway Climate</div>

    <ul class="contact-list">
      <li>555-214-6837
        <svg viewBox="0 0 24 24"><path d="M6.6 10.8a15 15 0 0 0 6.6 6.6l2.2-2.2a1 1 0 0 1 1-.25 11.4 11.4 0 0 0 3.6.6 1 1 0 0 1 1 1V20a1 1 0 0 1-1 1A17 17 0 0 1 3 4a1 1 0 0 1 1-1h3.5a1 1 0 0 1 1 1c0 1.25.2 2.45.6 3.6a1 1 0 0 1-.25 1z"/></svg></li>
      <li>info@BreezewayClimateLLC.example
        <svg viewBox="0 0 24 24"><path d="M2 5h20v14H2z M2 5l10 8 10-8" stroke="#fff" stroke-width="1.5"/></svg></li>
      <li>www.BreezewayClimateLLC.example
        <svg viewBox="0 0 24 24"><circle cx="12" cy="12" r="10"/></svg></li>
      <li>PO box 618 <span class="spacer"></span></li>
      <li>Millbrook NJ 07999
        <svg viewBox="0 0 24 24"><path d="M12 2a7 7 0 0 0-7 7c0 5 7 13 7 13s7-8 7-13a7 7 0 0 0-7-7zm0 9.5A2.5 2.5 0 1 1 12 6.5a2.5 2.5 0 0 1 0 5z"/></svg></li>
    </ul>

    <p class="holder-name">Dominic Vasquerelli</p>
  </section>
</main>
</body>
</html>
```